Mobile Home Page Design for “Zarvo for Plumbers” – in Figma

PipeDashly: Fast, Reliable Emergency Plumbing at Your Fingertips

PipeDashly is a streamlined platform connecting homeowners with trusted, local plumbers for urgent repairs—whether it’s a burst pipe, leak, or blocked toilet. Designed for speed and peace of mind, our homepage will be clean, modern, and mobile-optimized to guide users from problem to solution in minutes.

Our primary users are homeowners in stressful situations who care most about price transparency and how fast help can arrive. Bookings are made exclusively online, so the user experience must instill confidence and eliminate hesitation.

The call-to-action should be immediate and persuasive—"See Prices & Book" will be prominently featured as the main CTA. Additional trust-builders could include:

A simple 3-step booking illustration (Tell us what’s wrong → See prices → Get a plumber)
Customer reviews or “Trusted by 10,000+ homeowners” badges

Display real-time availability ("Next plumber available in 40 minutes")
Price estimates upfront—with clear service types

Target Market(s)

Home Owners: 35-65 Years old.

Industry/Entity Type

Home Services.

Number of Pages Required

1 page

Font styles to use
Sans Serif

Colors
0054AA
0677BA
7BADD7
CADEEF
E8F1F8
FFF300
FFF600
FEFA6F
FFFEC7
FFFEE8

Requirements
Nice to have
• Map showing that plumbers are nearby. Trustworthy look and feel. Blue/Red or Blue/Yellow.

```html
<!DOCTYPE html>
<html lang="en">
<head>
<meta charset="UTF-8">
<title>PipeDashly – Home</title>
<link href="https://fonts.googleapis.com/css2?family=Outfit:wght@400;500;600&family=Roboto:wght@400&display=swap" rel="stylesheet">
<style>
  :root {
    --page-bg: #ffffff;
    --ink: #111111;
    --ink-soft: #2a2a2a;
    --rule: #d9d9de;
    --blue: #0650f4;
    --red: #f4101c;
    --on-card: #ffffff;
  }
  * { box-sizing: border-box; margin: 0; padding: 0; }
  html, body { width: 900px; height: 1200px; overflow: hidden; }
  body {
    background: var(--page-bg);
    font-family: "Outfit", sans-serif;
    color: var(--ink);
    position: relative;
  }
  .section-label {
    position: absolute; left: 56px; top: 36px;
    font-family: "Roboto", sans-serif;
    font-size: 24px; letter-spacing: 0.2px;
    color: var(--ink-soft);
  }
  .trust-list { position: absolute; left: 50px; right: 50px; top: 96px; list-style: none; }
  .trust-item {
    position: relative; height: 162px;
    border-top: 1.5px solid var(--rule);
    display: flex; align-items: center;
  }
  .trust-icon { width: 68px; height: 68px; margin-left: 40px; }
  .trust-text { position: absolute; left: 390px; top: 50%; transform: translateY(-50%); }
  .trust-title { font-size: 48px; font-weight: 500; line-height: 1.05; }
  .trust-sub { font-size: 27px; font-weight: 400; color: var(--ink-soft); margin-top: 6px; }

  .service-card {
    position: absolute; left: 50px; right: 50px;
    height: 262px; border-radius: 30px;
    color: var(--on-card);
    padding: 32px 48px 40px;
  }
  .service-card.blue { background: var(--blue); }
  .service-card.red { background: var(--red); }
  .service-icon { width: 38px; height: 38px; display: block; }
  .service-title { font-size: 36px; font-weight: 600; line-height: 1.2; margin-top: 20px; }
  .service-text { font-size: 27px; font-weight: 400; line-height: 1.4; margin-top: 14px; max-width: 620px; }
  .card-plumbing { top: 600px; }
  .card-heating { top: 888px; }
  .card-next { top: 1176px; }
</style>
</head>
<body>
  <p class="section-label">ALL OUR PLUMBERS ARE</p>

  <ul class="trust-list">
    <li class="trust-item">
      <svg class="trust-icon" viewBox="0 0 72 72" fill="none" stroke="#111" stroke-width="3.5" stroke-linejoin="round">
        <polygon points="36,6 45,15 58,14 57,27 66,36 57,45 58,58 45,57 36,66 27,57 14,58 15,45 6,36 15,27 14,14 27,15"/>
        <text x="36" y="46" text-anchor="middle" font-family="Outfit, sans-serif" font-size="28" font-weight="600" fill="#111" stroke="none">5</text>
      </svg>
      <div class="trust-text">
        <div class="trust-title">Min 5 Yrs</div>
        <div class="trust-sub">in experience</div>
      </div>
    </li>
    <li class="trust-item">
      <svg class="trust-icon" viewBox="0 0 72 72" fill="none" stroke="#111" stroke-width="3.5" stroke-linecap="round">
        <circle cx="30" cy="22" r="10"/>
        <path d="M12 58v-6c0-9 8-15 18-15 6 0 11 2 14 6"/>
        <path d="M52 44v12M46 50h12M48 46l8 8M56 46l-8 8" stroke-width="3"/>
      </svg>
      <div class="trust-text">
        <div class="trust-title">Vetted</div>
        <div class="trust-sub">lipsum dolor</div>
      </div>
    </li>
    <li class="trust-item">
      <svg class="trust-icon" viewBox="0 0 72 72" fill="none" stroke="#111" stroke-width="3.5" stroke-linecap="round" stroke-linejoin="round">
        <path d="M8 34C8 20 20 10 36 10s28 10 28 24c-4-4-9-4-13 0-4-4-11-4-15 0-4-4-11-4-15 0-4-4-9-4-13 0z"/>
        <path d="M36 34v24c0 6-9 6-9 0"/>
        <path d="M36 6v4"/>
      </svg>
      <div class="trust-text">
        <div class="trust-title">Insured</div>
        <div class="trust-sub">lipsum dolor amet</div>
      </div>
    </li>
  </ul>

  <section class="service-card blue card-plumbing">
    <svg class="service-icon" viewBox="0 0 40 40" fill="none" stroke="#fff" stroke-width="3" stroke-linecap="round" stroke-linejoin="round">
      <path d="M6 14h16c4 0 6 3 6 6v4"/>
      <path d="M6 10v8M14 8h6M17 8v6"/>
      <path d="M28 30v1M25 34v1M31 34v1"/>
    </svg>
    <h2 class="service-title">Plumbing</h2>
    <p class="service-text">We offer all solutions to all your plumbing problems from leaks to blocked toilets</p>
  </section>

  <section class="service-card red card-heating">
    <svg class="service-icon" viewBox="0 0 40 40" fill="none" stroke="#fff" stroke-width="3" stroke-linecap="round">
      <path d="M10 6v18a5 5 0 1 0 4 0V6a2 2 0 0 0-4 0z"/>
      <path d="M24 6v18a5 5 0 1 0 4 0V6a2 2 0 0 0-4 0z"/>
    </svg>
    <h2 class="service-title">Heating</h2>
    <p class="service-text">We offer all solutions to all your plumbing problems from leaks to blocked toilets</p>
  </section>

  <section class="service-card blue card-next">
    <svg class="service-icon" viewBox="0 0 40 40" fill="none" stroke="#fff" stroke-width="3" stroke-linecap="round" stroke-linejoin="round">
      <path d="M12 6v22h18v-4c0-3-4-4-8-5l-4-2V6z"/>
    </svg>
  </section>
</body>
</html>
```